My company is throwing a party. The name is 75/25 (75% Reggae & 25% Whatever Remains)

I seek a flyer that shows this will be a very elegant, upscale event and at the same time high energy, great reggae music and dancing.

I need this flyer to be 650 pixels wide & any length, High resolution (1MB) for printing on a 4" x 6" flyer.

Target Market(s)

Fans of reggae music

Industry/Entity Type

Printing

Requirements
Must have
• Radiant Holdings Presents:
75/25
Upscale Reggae Soiree
75% Reggae - 25% Whatever Remains

Saturday May 4th, 10pm - 3am

The Larkmill: 418 1/2 North Calloway Blvd, OKC

Dress to impress! We reserve the right to refuse entry

Free Entry: 1st 50 Ladies On VIP Guestlist - Discounted Early Bird Online Tickets - For Bottle Service Reservation: http://islandnightsmx.ticketloom.example

More info? 405-817-2690

```html
<!DOCTYPE html>
<html lang="en">
<head>
<meta charset="utf-8">
<title>75/25 – Upscale Reggae Soiree</title>
<link href="https://fonts.googleapis.com/css2?family=Archivo+Black&family=Montserrat:wght@500;700&family=Passion+One:wght@900&display=swap" rel="stylesheet">
<style>
  :root {
    --rasta-red: #e3232a;
    --rasta-yellow: #f7e01c;
    --rasta-green: #2fa83c;
    --deep-green: #128a2e;
    --ink: #0d0d0d;
    --paper: #ffffff;
    --shadow: rgba(0,0,0,0.55);
  }
  html, body {
    margin: 0;
    padding: 0;
    width: 1200px;
    height: 2702px;
    overflow: hidden;
    background: #ffffff;
  }
  .flyer {
    position: relative;
    width: 1200px;
    height: 2702px;
    overflow: hidden;
    background: linear-gradient(90deg,
      var(--rasta-red) 0%, var(--rasta-red) 34%,
      #f28a1e 42%, var(--rasta-yellow) 50%, var(--rasta-yellow) 56%,
      #9ccb2a 64%, var(--rasta-green) 72%, var(--deep-green) 100%);
    font-family: "Archivo Black", "Arial Black", sans-serif;
  }
  .photo-area {
    position: absolute;
    left: 150px; top: 0;
    width: 1050px; height: 1150px;
    background: radial-gradient(ellipse 48% 42% at 55% 38%, rgba(10,10,10,0.92) 0%, rgba(20,20,20,0.75) 45%, rgba(20,20,20,0) 80%);
  }
  .record-area {
    position: absolute;
    left: 280px; top: 1560px;
    width: 760px; height: 760px;
    border-radius: 50%;
    background: radial-gradient(circle, rgba(245,200,30,0.0) 8%, rgba(235,180,20,0.55) 10%, rgba(250,215,40,0.35) 40%, rgba(250,225,40,0) 70%);
  }
  .guitar-area {
    position: absolute;
    left: 930px; top: 1850px;
    width: 230px; height: 650px;
    background: linear-gradient(180deg, rgba(10,90,30,0) 0%, rgba(10,90,30,0.45) 50%, rgba(10,90,30,0) 100%);
    border-radius: 40% 40% 45% 45%;
  }
  .presenter {
    position: absolute;
    top: 88px; left: 0; width: 100%;
    margin: 0;
    text-align: center;
    color: var(--paper);
    font-family: "Montserrat", Arial, sans-serif;
    font-weight: 500;
    font-size: 58px;
    line-height: 1.12;
    letter-spacing: 1px;
    text-transform: uppercase;
  }
  .title-art {
    position: absolute;
    left: 0; top: 0;
    width: 1200px; height: 2702px;
    pointer-events: none;
  }
  .headline-number {
    font-family: "Passion One", "Arial Black", sans-serif;
    font-weight: 900;
    font-size: 600px;
    fill: var(--paper);
    filter: drop-shadow(6px 8px 0 rgba(0,0,0,0.55));
  }
  .tagline {
    font-family: "Archivo Black", "Arial Black", sans-serif;
    fill: var(--ink);
    stroke: var(--paper);
    stroke-width: 8px;
    stroke-linejoin: round;
    paint-order: stroke fill;
    filter: drop-shadow(5px 7px 0 rgba(0,0,0,0.5));
  }
  .tagline-major { font-size: 150px; }
  .tagline-minor { font-size: 92px; }
  .soiree {
    font-family: "Montserrat", Arial, sans-serif;
    font-weight: 700;
    font-size: 44px;
    letter-spacing: 4px;
    fill: var(--paper);
    filter: drop-shadow(3px 4px 0 rgba(0,0,0,0.6));
  }
  .event-time {
    position: absolute;
    left: 575px; top: 1490px;
    margin: 0;
    color: var(--paper);
    font-size: 82px;
    line-height: 0.98;
    text-align: center;
    transform: rotate(3deg);
    text-shadow: 4px 5px 0 var(--ink);
  }
  .details {
    position: absolute;
    left: 180px; top: 1830px;
    width: 900px;
    color: var(--ink);
    font-family: "Archivo Black", "Arial Black", sans-serif;
    font-size: 38px;
    line-height: 1.08;
    transform: rotate(3deg);
    transform-origin: left top;
  }
  .details p { margin: 0 0 34px; }
  .contact-band {
    position: absolute;
    left: 90px; top: 2520px;
    width: 1035px; height: 136px;
    background: var(--paper);
    clip-path: polygon(0 6%, 22% 0, 55% 4%, 100% 0, 99% 95%, 60% 100%, 30% 96%, 1% 100%);
    display: flex;
    align-items: center;
    justify-content: center;
    gap: 22px;
    font-size: 66px;
    box-sizing: border-box;
    padding-top: 6px;
  }
  .contact-band .label { color: var(--rasta-red); }
  .contact-band .phone { color: var(--ink); }
</style>
</head>
<body>
<main class="flyer">
  <div class="photo-area" role="img" aria-label="Photograph of a reggae singer with dreadlocks"></div>
  <div class="record-area" role="img" aria-label="Illustration of a vinyl record"></div>
  <div class="guitar-area" role="img" aria-label="Illustration of an electric guitar"></div>

  <h2 class="presenter">Radiant Holdings<br>Presents</h2>

  <svg class="title-art" viewBox="0 0 1200 2702" xmlns="http://www.w3.org/2000/svg">
    <text class="headline-number" x="600" y="1095" text-anchor="middle" textLength="1000" lengthAdjust="spacingAndGlyphs">75/25</text>
    <g transform="rotate(-8 100 1270)">
      <text class="tagline tagline-major" x="100" y="1270" textLength="900" lengthAdjust="spacingAndGlyphs">75% Reggae</text>
      <text class="tagline tagline-minor" x="80" y="1380" textLength="980" lengthAdjust="spacingAndGlyphs">25% Whatever Remains</text>
      <text class="soiree" x="110" y="1448" textLength="560" lengthAdjust="spacingAndGlyphs">UPSCALE REGGAE SOIREE</text>
    </g>
  </svg>

  <p class="event-time">Saturday<br>May 4th<br>10pm - 3am</p>

  <section class="details">
    <p>The Larkmill:<br>418 1/2 North Calloway Blvd, OKC</p>
    <p>Dress to impress!<br>We reserve the right to refuse<br>entry</p>
    <p>Free Entry: 1st 50 Ladies On VIP<br>Guestlist - Discounted Early Bird</p>
    <p>Online Tickets - For Bottle<br>Service Reservation:<br>http://islandnightsmx.ticketloom.example</p>
  </section>

  <div class="contact-band">
    <span class="label">More info?</span>
    <span class="phone">405-817-2690</span>
  </div>
</main>
</body>
</html>
```